Veltrium stationery design

Design stationery for us that fits with the colours of the logo. We are looking for letterheads, business cards etc. Something we can use for a prospectus and marketing presentations in power point. Must be completed in such a manner that it represents a corporate image for large enterprise clients and other large organisations. The company is a project assurance and monitoring company that works in all industries.

```html
<!DOCTYPE html>
<html lang="en">
<head>
<meta charset="utf-8">
<title>Veltrium Stationery</title>
<link href="https://fonts.googleapis.com/css2?family=Poppins:wght@300;400;500;600;700;800&display=swap" rel="stylesheet">
<style>
  :root {
    --night: #010d24;
    --paper: #ffffff;
    --navy: #0b2f6b;
    --blue: #1466b8;
    --sky: #1a82d0;
    --red: #e8120c;
    --orange: #ff5a0a;
    --amber: #ff9a0a;
    --ink: #2a2a2a;
    --muted: #555;
  }
  * { margin: 0; padding: 0; box-sizing: border-box; }
  html, body { width: 1200px; height: 1200px; overflow: hidden; background: var(--night); }
  body { position: relative; font-family: 'Poppins', sans-serif; color: var(--ink); }

  .section-title { position: absolute; color: #fff; font-weight: 400; white-space: nowrap; transform: translateX(-50%); letter-spacing: 0.5px; }
  .section-title--letterhead { left: 431px; top: 128px; font-size: 37px; }
  .section-title--cards { left: 965px; top: 350px; font-size: 37px; }

  .letterhead { position: absolute; left: 102px; top: 214px; width: 658px; height: 852px; background: var(--paper); overflow: hidden; }
  .letterhead .abs { position: absolute; }

  .brand { display: flex; align-items: center; gap: 8px; white-space: nowrap; }
  .brand__dot { border-radius: 50%; background: var(--orange); flex: none; }
  .brand__name { font-weight: 700; color: var(--navy); text-transform: uppercase; letter-spacing: 0.5px; }

  .letterhead__brand { left: 72px; top: 58px; }
  .letterhead__brand .brand__dot { width: 34px; height: 34px; }
  .letterhead__brand .brand__name { font-size: 25px; }

  .header-rule { left: 360px; top: 74px; width: 298px; height: 4px; background: var(--navy); }
  .header-rule::after { content: ""; position: absolute; right: 0; top: -8px; width: 110px; height: 4px; background: var(--orange); }

  .recipient__to { left: 80px; top: 175px; font-size: 10px; }
  .recipient__role { left: 80px; top: 190px; font-size: 6.2px; letter-spacing: 1.3px; color: var(--muted); }
  .recipient__name { left: 80px; top: 199px; font-size: 16px; font-weight: 800; color: var(--red); }
  .recipient__degree { left: 80px; top: 218px; font-size: 9.3px; color: var(--ink); }
  .letter-date { right: 76px; top: 218px; font-size: 10px; font-weight: 600; }
  .letter-date span { color: var(--red); }

  .letter-body { left: 79px; top: 256px; width: 502px; font-size: 9.6px; line-height: 11.65px; text-align: justify; color: #333; }
  .letter-body p + p { margin-top: 11.5px; }

  .closing { left: 80px; top: 594px; font-size: 12px; font-weight: 700; color: var(--blue); }
  .signature { left: 80px; top: 618px; width: 140px; height: 44px; border-radius: 4px; background: linear-gradient(90deg, #ececec, #f6f6f6); }

  .contact-row { left: 80px; top: 725px; display: flex; gap: 12px; font-size: 10.3px; white-space: nowrap; align-items: center; }
  .contact { display: flex; align-items: center; gap: 5px; white-space: nowrap; }
  .icon { flex: none; display: block; }

  .footer-band { left: 0; bottom: 0; width: 658px; height: 42px; }
  .footer-band__line { position: absolute; left: 0; top: 6px; width: 658px; height: 3px; background: var(--orange); }
  .footer-band__bar { position: absolute; left: 0; bottom: 0; width: 658px; height: 22px; background: linear-gradient(90deg, var(--sky), var(--navy)); }
  .footer-band__accent { position: absolute; right: 0; bottom: 0; width: 180px; height: 22px; background: linear-gradient(90deg, var(--amber), var(--orange)); }

  .card { position: absolute; left: 820px; width: 290px; height: 165px; background: var(--paper); overflow: hidden; }
  .card--front { top: 419px; }
  .card--back { top: 628px; }
  .card .abs { position: absolute; }
  .card--front .brand { left: 50%; top: 60px; transform: translateX(-50%); }
  .card--front .brand__dot { width: 26px; height: 26px; }
  .card--front .brand__name { font-size: 17px; }
  .card__url { left: 0; width: 100%; top: 120px; text-align: center; font-size: 9.5px; letter-spacing: 1.2px; }

  .card-band { left: 0; bottom: 0; width: 290px; height: 24px; }
  .card-band__line { position: absolute; left: 0; top: 0; width: 290px; height: 2px; background: var(--orange); }
  .card-band__bar { position: absolute; left: 0; bottom: 0; width: 290px; height: 16px; background: var(--navy); }
  .card-band__accent { position: absolute; bottom: 0; width: 90px; height: 16px; background: linear-gradient(90deg, var(--amber), var(--red)); }
  .card--front .card-band__accent { right: 0; }
  .card--back .card-band__accent { left: 0; }

  .card--back .brand { right: 20px; top: 20px; gap: 5px; }
  .card--back .brand__dot { width: 13px; height: 13px; }
  .card--back .brand__name { font-size: 9px; }
  .card__name { left: 24px; top: 50px; font-size: 11px; font-weight: 800; color: var(--red); white-space: nowrap; }
  .card__name span { color: var(--navy); }
  .card__title { left: 24px; top: 65px; font-size: 5.6px; color: var(--muted); }
  .card__divider { left: 140px; top: 60px; width: 130px; height: 1px; background: #c4c4c4; }
  .card__contacts { left: 24px; top: 89px; display: grid; grid-template-columns: 109px auto; row-gap: 6px; font-size: 6.4px; }
  .card__contacts .contact { gap: 4px; }
</style>
</head>
<body>

<h1 class="section-title section-title--letterhead">Letterhead Design</h1>
<h2 class="section-title section-title--cards">Business Cards</h2>

<section class="letterhead">
  <div class="abs brand letterhead__brand">
    <span class="brand__dot"></span><span class="brand__name">Veltrium</span>
  </div>
  <div class="abs header-rule"></div>

  <div class="abs recipient__to">To</div>
  <div class="abs recipient__role">Founder &amp; Lead Researcher</div>
  <div class="abs recipient__name">Dr. Marcus van Riel</div>
  <div class="abs recipient__degree">Doctor of Management in Technology and Innovation</div>
  <div class="abs letter-date"><span>Date:</span> 23.07.2026</div>

  <div class="abs letter-body">
    <p>Lorem Ipsum is simply dummy text of the printing and typesetting industry. Lorem Ipsum has been the industry's standard dummy text ever since 1966, when designers at Typeline and Henry Calder, the librarian at Fleetmark Printing Library in London, took a 1914 Cicero translation and scrambled it to make dummy text for Typeline's Body Type sheets. It has survived not only many decades, but also the leap into electronic typesetting, remaining essentially unchanged. It was popularised thanks to these sheets and more recently with desktop publishing software like PageForm and WordDesk including versions of Lorem Ipsum. Lorem Ipsum is simply dummy text of the printing and typesetting industry. Lorem Ipsum has been the industry's standard dummy text ever since 1966, when designers at Typeline and Henry Calder, the librarian at Fleetmark Printing Library in London, took a 1914 Cicero translation and scrambled it to make dummy text for Typeline's Body Type sheets. It has survived not only many decades, but also the leap into electronic typesetting, remaining essentially unchanged. It was popularised thanks to these sheets and more recently with desktop publishing software like PageForm and WordDesk including versions of Lorem Ipsum.</p>
    <p>Lorem Ipsum is simply dummy text of the printing and typesetting industry. Lorem Ipsum has been the industry's standard dummy text ever since 1966, when designers at Typeline and Henry Calder, the librarian at Fleetmark Printing Library in London, took a 1914 Cicero translation and scrambled it to make dummy text for Typeline's Body Type sheets. It has survived not only many decades, but also the leap into electronic typesetting, remaining essentially unchanged. It was popularised thanks to these sheets and more recently with desktop publishing software like PageForm and WordDesk including versions of Lorem Ipsum.</p>
    <p>Lorem Ipsum is simply dummy text of the printing and typesetting industry. Lorem Ipsum has been the industry's standard dummy text ever since 1966, when designers at Typeline and Henry Calder, the librarian at Fleetmark Printing Library in London, took a 1914 Cicero translation and scrambled it to make dummy text for Typeline's Body Type sheets.</p>
  </div>

  <div class="abs closing">Yours Sincerely</div>
  <div class="abs signature" role="img" aria-label="Handwritten signature of the sender"></div>

  <div class="abs contact-row">
    <span class="contact">
      <svg class="icon" width="16" height="16" viewBox="0 0 16 16"><circle cx="8" cy="8" r="7" fill="none" stroke="var(--orange)" stroke-width="1.6"/><path d="M5.5 4.5c-.6.6-.5 2 .8 3.6s2.9 2.6 3.7 2.3l.8-.9-1.5-1.1-.7.5c-.7-.3-1.5-1.1-1.8-1.8l.5-.7-1.1-1.5z" fill="var(--orange)"/></svg>
      014.582.3367</span>
    <span class="contact">
      <svg class="icon" width="16" height="16" viewBox="0 0 16 16"><circle cx="8" cy="8" r="7" fill="none" stroke="var(--orange)" stroke-width="1.6"/><path d="M8 3.8a2.6 2.6 0 0 0-2.6 2.6C5.4 8.4 8 11.6 8 11.6s2.6-3.2 2.6-5.2A2.6 2.6 0 0 0 8 3.8z" fill="var(--orange)"/><circle cx="8" cy="6.4" r="1" fill="#fff"/></svg>
      Headquarters in Valletta</span>
    <span class="contact">
      <svg class="icon" width="16" height="16" viewBox="0 0 16 16"><circle cx="8" cy="8" r="7" fill="none" stroke="var(--orange)" stroke-width="1.6"/><rect x="4.6" y="5.5" width="6.8" height="5" rx=".6" fill="none" stroke="var(--orange)" stroke-width="1"/><path d="M4.8 5.8 8 8.3l3.2-2.5" fill="none" stroke="var(--orange)" stroke-width="1"/></svg>
      info@veltrium.com</span>
    <span class="contact">
      <svg class="icon" width="16" height="16" viewBox="0 0 16 16"><circle cx="8" cy="8" r="7" fill="none" stroke="var(--orange)" stroke-width="1.6"/><circle cx="8" cy="8" r="3.4" fill="none" stroke="var(--orange)" stroke-width="1"/><path d="M4.6 8h6.8M8 4.6c-1.6 2-1.6 4.8 0 6.8M8 4.6c1.6 2 1.6 4.8 0 6.8" fill="none" stroke="var(--orange)" stroke-width=".8"/></svg>
      www.veltrium.com</span>
  </div>

  <div class="abs footer-band">
    <div class="footer-band__line"></div>
    <div class="footer-band__bar"></div>
    <div class="footer-band__accent"></div>
  </div>
</section>

<section class="card card--front">
  <div class="abs brand">
    <span class="brand__dot"></span><span class="brand__name">Veltrium</span>
  </div>
  <div class="abs card__url">www.veltrium.com</div>
  <div class="abs card-band">
    <div class="card-band__line"></div>
    <div class="card-band__bar"></div>
    <div class="card-band__accent"></div>
  </div>
</section>

<section class="card card--back">
  <div class="abs brand">
    <span class="brand__dot"></span><span class="brand__name">Veltrium</span>
  </div>
  <div class="abs card__name">Dr. Marcus van <span>Riel</span></div>
  <div class="abs card__title">Founder &amp; Lead Researcher</div>
  <div class="abs card__divider"></div>

  <div class="abs card__contacts">
    <span class="contact"><svg class="icon" width="10" height="10" viewBox="0 0 16 16"><circle cx="8" cy="8" r="7" fill="none" stroke="var(--orange)" stroke-width="2"/><path d="M5.5 4.5c-.6.6-.5 2 .8 3.6s2.9 2.6 3.7 2.3l.8-.9-1.5-1.1-.7.5c-.7-.3-1.5-1.1-1.8-1.8l.5-.7-1.1-1.5z" fill="var(--orange)"/></svg>014.582.3367</span>
    <span class="contact"><svg class="icon" width="10" height="10" viewBox="0 0 16 16"><circle cx="8" cy="8" r="7" fill="none" stroke="var(--orange)" stroke-width="2"/><rect x="4.6" y="5.5" width="6.8" height="5" fill="none" stroke="var(--orange)" stroke-width="1.2"/></svg>info@veltrium.com</span>
    <span class="contact"><svg class="icon" width="10" height="10" viewBox="0 0 16 16"><circle cx="8" cy="8" r="7" fill="none" stroke="var(--orange)" stroke-width="2"/><path d="M8 3.8a2.6 2.6 0 0 0-2.6 2.6C5.4 8.4 8 11.6 8 11.6s2.6-3.2 2.6-5.2A2.6 2.6 0 0 0 8 3.8z" fill="var(--orange)"/></svg>Headquarters in Valletta</span>
    <span class="contact"><svg class="icon" width="10" height="10" viewBox="0 0 16 16"><circle cx="8" cy="8" r="7" fill="none" stroke="var(--orange)" stroke-width="2"/><circle cx="8" cy="8" r="3.4" fill="none" stroke="var(--orange)" stroke-width="1.2"/></svg>www.veltrium.com</span>
  </div>

  <div class="abs card-band">
    <div class="card-band__line"></div>
    <div class="card-band__bar"></div>
    <div class="card-band__accent"></div>
  </div>
</section>

</body>
</html>
```